Hello my name is Colin, I am Starting a business called Harbor Health and fitness and am in need of a memorable business card.
It is a personal training studio. I have added the logo that i would like to be on the left center om my business card. i would like room left up the top for a heading sentence such as. "Is your body shocking for all the wrong reasons". there must be room left on the right of the logo below the main heading for 3 sub headings.
then under those 3 headings and logo room for another larger heading eg. "give me a call and learn how to eat chocolate, drink bear and have great sex". in what room is left i would like to be used for my contact details, use I'm Colin Pettersby your fitness expert on the left then on the right Phone, Email and website space in at least 12 Point. Very specific i know :) now onto the back, for the back i would like an eye catching graphic and room for one main headline and 3 bullet points centered just write anything i will choose what to put in them when i pick a winner. Thank you very much for sticking through all of that :) i appreciate you taking the time to read it and hopefully undergo designing me a business card.
I can't wait to see the designs!

Target Market(s)

slightly more towards females although it would probably be best if it was targeted towards both sexes

Industry/Entity Type

Training

Requirements
Nice to have
• I would love to see if anyone could come up with a design that would really make my card stand out and be memorable.
Should not have
• tacky fitness photos of abs and muscles etc.

```html
<!DOCTYPE html>
<html lang="en">
<head>
<meta charset="utf-8">
<title>Harbor Health and fitness – Business Card</title>
<link href="https://fonts.googleapis.com/css2?family=Montserrat:wght@400;500;700;800&display=swap" rel="stylesheet">
<style>
  :root {
    --navy: #0d3a6e;
    --navy-deep: #082a52;
    --navy-light: #1f5a9a;
    --ink: #2a2f38;
    --muted: #555b66;
    --paper: #ffffff;
    --ghost: #d9dbde;
    --backdrop: #e9ebee;
  }
  * { margin: 0; padding: 0; box-sizing: border-box; }
  html, body {
    width: 1200px; height: 1024px; overflow: hidden;
    background: var(--backdrop);
    font-family: "Montserrat", Arial, sans-serif;
  }
  .canvas { position: relative; width: 1200px; height: 1024px; }

  .card {
    position: absolute; left: 220px; width: 760px; height: 434px;
    overflow: hidden; box-shadow: 0 6px 18px rgba(0,0,0,0.18);
  }
  .card--front { top: 52px; background: var(--paper); }
  .card--back {
    top: 538px;
    background: radial-gradient(ellipse at 35% 40%, var(--navy-light) 0%, var(--navy) 45%, var(--navy-deep) 100%);
  }

  /* Front */
  .front-band { position: absolute; right: 0; top: 0; width: 120px; height: 434px; }
  .front-figures {
    position: absolute; left: 430px; top: 0; width: 210px; height: 170px;
    background: radial-gradient(ellipse at 50% 45%, var(--ghost) 0%, rgba(217,219,222,0.4) 55%, rgba(255,255,255,0) 75%);
  }
  .headline {
    position: absolute; left: 34px; top: 42px;
    color: var(--navy); font-weight: 800; font-size: 19px; letter-spacing: 0;
    white-space: nowrap;
  }
  .subline {
    position: absolute; left: 34px; top: 70px;
    color: var(--ink); font-weight: 700; font-size: 11px; letter-spacing: 0.1px;
    white-space: nowrap;
  }
  .brand {
    position: absolute; right: 140px; top: 140px; color: var(--navy); font-weight: 500;
    line-height: 1; text-align: right;
  }
  .brand__name { font-size: 64px; letter-spacing: -1px; }
  .brand__tag { font-size: 17px; margin-top: 6px; }

  .contact { position: absolute; left: 34px; top: 268px; color: var(--ink); }
  .contact__name { color: var(--navy); font-weight: 800; font-size: 22px; }
  .contact__role { font-size: 16px; color: var(--muted); margin-top: 2px; }
  .contact__list { list-style: none; margin-top: 14px; }
  .contact__item {
    display: flex; align-items: center; gap: 10px;
    font-size: 17px; color: var(--ink); margin-bottom: 6px;
  }
  .contact__icon { width: 16px; height: 16px; fill: var(--navy); }

  /* Back */
  .back-figures {
    position: absolute; left: 40px; top: 0; width: 520px; height: 170px;
    background: radial-gradient(ellipse at 50% 40%, rgba(70,130,200,0.55) 0%, rgba(40,95,160,0.25) 50%, rgba(13,58,110,0) 75%);
  }
  .back-brand {
    position: absolute; left: 250px; top: 190px; color: var(--paper); font-weight: 500; line-height: 1;
  }
  .back-brand__name { font-size: 96px; letter-spacing: -1px; }
  .back-brand__tag { font-size: 22px; margin-top: 8px; }
  .back-brand__web { font-size: 15px; margin-top: 6px; letter-spacing: 0.5px; }
</style>
</head>
<body>
<main class="canvas">

  <section class="card card--front" aria-label="Business card front">
    <svg class="front-band" viewBox="0 0 120 434" aria-hidden="true">
      <path d="M70 0 C40 140 40 300 60 434 L120 434 L120 0 Z" fill="var(--navy)"/>
      <path d="M58 0 C30 140 30 300 48 434 L54 434 C36 300 36 140 64 0 Z" fill="var(--navy-light)"/>
    </svg>
    <div class="front-figures" role="img" aria-label="Faint grey silhouettes of people exercising"></div>

    <h1 class="headline">IS YOUR BODY SHOCKING FOR ALL THE WRONG REASONS</h1>
    <p class="subline">GIVE ME A CALL AND LEARN HOW TO EAT CHOCOLATE DRINK BEAR AND HAVE GREAT SEX</p>

    <div class="brand">
      <div class="brand__name">Harbor</div>
      <div class="brand__tag">Health and Fitness</div>
    </div>

    <div class="contact">
      <h2 class="contact__name">Colin Pettersby</h2>
      <p class="contact__role">fitness expert</p>
      <ul class="contact__list">
        <li class="contact__item">
          <svg class="contact__icon" viewBox="0 0 24 24" aria-hidden="true"><path d="M6.6 10.8a15.1 15.1 0 0 0 6.6 6.6l2.2-2.2a1 1 0 0 1 1-.25 11.4 11.4 0 0 0 3.6.57 1 1 0 0 1 1 1V20a1 1 0 0 1-1 1A17 17 0 0 1 3 4a1 1 0 0 1 1-1h3.5a1 1 0 0 1 1 1c0 1.25.2 2.45.57 3.57a1 1 0 0 1-.25 1z"/></svg>
          000 -000-000
        </li>
        <li class="contact__item">
          <svg class="contact__icon" viewBox="0 0 24 24" aria-hidden="true"><path d="M2 5h20v14H2z M2 5l10 8 10-8" fill="var(--navy)" stroke="#fff" stroke-width="1.2"/></svg>
          hello@harborfit.com
        </li>
        <li class="contact__item">
          <svg class="contact__icon" viewBox="0 0 24 24" aria-hidden="true"><circle cx="12" cy="12" r="10"/><path d="M2 12h20M12 2c3 3 3 17 0 20M12 2c-3 3-3 17 0 20" stroke="#fff" stroke-width="1.3" fill="none"/></svg>
          www.harborfit.com
        </li>
      </ul>
    </div>
  </section>

  <section class="card card--back" aria-label="Business card back">
    <div class="back-figures" role="img" aria-label="Faint blue silhouettes of people exercising"></div>
    <div class="back-brand">
      <div class="back-brand__name">Harbor</div>
      <div class="back-brand__tag">Health and Fitness</div>
      <div class="back-brand__web">www.harborfit.com</div>
    </div>
  </section>

</main>
</body>
</html>
```